Company Presentation re-design.

We need to create a new 15-20 pager-presentation that will show KORVALE (travel management company) as a client-centric company with a human-to-human approach. As a start we ask a Designers to create a 3 page test presentation so we can choose the winner. who will then design the rest slides

Two main idears are to be shown on the slides:
• KORVALE is client-centric company who believes in partnership with corporate clients;
• KORVALE is a stable and trustworthy partner;

The test slides should be:

Slide (1) - Our strategy is Customer – centric strategy. KORVALE bases its business approach on the customer needs. 5 qualities that identify KORVALE as a customer-centric :
1. corporate culture, aimed at customers' changing needs
2. professional Key Account Manager (KAM)
3. Each product solution meets specific client needs.
4. innovation
5. security policy

Slide (2) - Our product solutions of clients needs
The main idea of this page is to describe our products for customers. KORVALE has 5 main products:
1. Business Travel
2. Service
3. On-line booking
4. MICE & Congress
5. Non-standard services

Slide (3)
This page shows the highlights of KORVALE support and it is shown in a cloud design now.

Attched pls find our current presentation

Dear Professionals! Please pay attantion that we updated the project by doubled the budjet! Wait for yiour grate ideas. 

Target Market(s)

Mid to top management (practically any industry), travel coordinators, procurement specialists, corporate buyers etc, travelers

Industry/Entity Type

Security

Requirements
Must have
• (1) The presentation must visualize the text above, with as little text itself as possible.
(2) We would appreciate ideas with INFOGRAPHIC
(3) Design of the presentation is up to the company logo in all variations. ( attached files).
(4) We would like to see designs that use grey, blue, orange and maroon colors - corporate colors of our logo.
Nice to have
• Infografics
Designs we like:
to brintaly.com+; zumoth.com; pelvanstudio.com; tarnowatt.co.uk (infografics)

```html
<!DOCTYPE html>
<html lang="en">
<head>
<meta charset="utf-8">
<title>KORVALE Travel — Test Presentation</title>
<link href="https://fonts.googleapis.com/css2?family=Roboto:wght@300;400;500;700&family=Roboto+Condensed:wght@700&display=swap" rel="stylesheet">
<style>
:root{
  --blue:#1a73b5;
  --blue-deep:#0f6ca8;
  --orange:#f58220;
  --grey:#7f7f80;
  --grey-dark:#58585a;
  --grey-light:#c9c9c9;
  --text:#333;
  --white:#fff;
}
*{box-sizing:border-box;margin:0;padding:0}
html,body{width:1200px;height:1000px;overflow:hidden;background:var(--white)}
body{position:relative;font-family:"Roboto",Arial,sans-serif;color:var(--text)}
.slide{position:absolute;width:552px;height:311px;border:1px solid #9a9a9a;background:var(--white);overflow:hidden}
.s1{left:39px;top:22px}.s2{left:612px;top:22px}
.s3{left:39px;top:343px}.s4{left:612px;top:343px}
.s5{left:39px;top:666px}.s6{left:612px;top:666px}

.corner{position:absolute;left:0;top:13px;width:38px;height:66px}
.slide-title{position:absolute;left:42px;top:25px;font-size:19px;font-weight:400;color:var(--grey)}
.slide-title b{color:var(--blue);font-weight:500}
.slide-title.solo{left:42px;color:var(--blue);font-weight:500}
.lead{position:absolute;left:42px;top:52px;font-size:11.5px;font-weight:700;color:var(--grey)}
.tag{position:absolute;right:24px;top:22px;font-size:7px;color:var(--grey);display:flex;align-items:center;gap:3px}
.tag span{display:inline-block;background:var(--grey);color:var(--white);font-weight:700;font-size:7.5px;padding:2px 3px}

.footer{position:absolute;left:0;bottom:0;width:100%;height:33px;background:var(--grey)}
.footer .brand{position:absolute;left:42px;top:7px;color:var(--white);font-weight:300;font-size:15px;line-height:1}
.footer .url{position:absolute;right:82px;top:9px;color:var(--white);font-size:13px}
.footer .nav{position:absolute;right:0;top:0;width:67px;height:33px;background:var(--blue-deep);display:flex;align-items:center;justify-content:center;gap:3px}
.nav svg{width:13px;height:13px}

.photo{position:absolute;border-radius:8px;border:1px solid #8c8c8c}
.ph-person{background:linear-gradient(180deg,#eef0f3 0%,#d7dbe2 40%,#3b4252 60%,#2c3240 100%)}
.ph-tray{background:linear-gradient(160deg,#f3f3f3 0%,#cfd9e4 35%,#8aa8c2 45%,#f2f2f2 60%,#1f1f1f 100%)}
.ph-laptop{background:linear-gradient(180deg,#fafafa 0%,#2d2d2d 25%,#3c5470 50%,#2d2d2d 70%,#d5d5d5 100%)}
.ph-congress{background:linear-gradient(180deg,#e4eaea 0%,#c4d6c2 45%,#6f8fa5 70%,#cdd6d8 100%)}
.ph-lady{background:linear-gradient(180deg,#f7f7f7 0%,#e9c3b3 25%,#d62a2a 50%,#c91f27 75%,#f2f2f2 100%)}
.ph-meeting{background:linear-gradient(135deg,#ece7e2 0%,#cbb6a2 30%,#2f3035 55%,#c4472f 75%,#e9e3dc 100%)}

/* cover */
.s1 .logo{position:absolute;left:67px;top:28px;color:var(--grey);font-weight:300;font-size:52px;line-height:1}
.s1 .logo small{display:block;text-align:right;font-size:14px;color:var(--blue);margin-top:-4px}
.s1 .claim{position:absolute;left:68px;top:134px;font-size:15.5px;font-weight:700;color:var(--grey)}
.s1 .sub{position:absolute;left:68px;top:153px;font-size:12.5px;color:var(--blue);line-height:1.08}
.s1 .band{position:absolute;left:0;top:201px;width:100%;height:110px;background:var(--blue-deep)}
.s1 .band-url{position:absolute;left:68px;top:45px;color:var(--white);font-size:15px;font-weight:500;letter-spacing:3px}
.s1 .hero{position:absolute;left:338px;top:10px;width:130px;height:290px;border-radius:40px 40px 6px 6px;background:linear-gradient(180deg,#d9c2b0 0%,#d9c2b0 12%,#2e3442 14%,#262b38 80%,#1a1d25 100%)}

/* strategy */
.s2 .lead{top:59px;width:490px;line-height:1.25}
.s2 .photo{left:42px;top:113px;width:180px;height:127px;border-radius:0}
.points{position:absolute;left:238px;top:107px;width:300px;list-style:none;font-size:6.8px;line-height:1.3;color:#222}
.points li{margin-bottom:4px}

/* products */
.cards{position:absolute;left:42px;top:89px;display:flex;gap:14px}
.card{width:84px;text-align:center}
.card .photo{position:relative;display:block;width:84px;height:116px}
.card p{margin-top:5px;font-size:11px;font-weight:700;color:var(--blue);line-height:1}

/* bullets */
.bullets{position:absolute;list-style:none;font-size:9px;line-height:1.75;color:#222}
.bullets li{position:relative;padding-left:17px;margin-bottom:11px}
.bullets li::before{content:"";position:absolute;left:2px;top:3px;width:7px;height:9px;background:var(--blue);clip-path:polygon(0 0,100% 50%,0 100%,30% 50%)}
.s4 .photo{left:42px;top:89px;width:117px;height:159px}
.s5 .photo{left:42px;top:90px;width:112px;height:156px}

/* closing */
.s6 .thanks{position:absolute;left:0;width:100%;top:26px;text-align:center;font-family:"Roboto Condensed",Arial,sans-serif;font-size:17px;color:var(--blue)}
.s6 .bubbles{position:absolute;left:200px;top:70px;width:152px;height:112px}
.s6 .base{position:absolute;left:0;top:201px;width:100%;height:110px;background:var(--grey)}
.s6 .base .brand{position:absolute;left:70px;top:28px;color:var(--white);font-weight:300;font-size:46px;line-height:1}
.s6 .base .brand small{display:block;text-align:right;font-size:14px;margin-top:-3px}
.s6 .base .rule{position:absolute;left:274px;top:22px;width:1px;height:70px;background:var(--white)}
.s6 .base address{position:absolute;left:300px;top:30px;font-style:normal;color:var(--white);font-size:12px;line-height:1.05}
</style>
</head>
<body>

<svg width="0" height="0" style="position:absolute" aria-hidden="true">
  <defs>
    <symbol id="corner" viewBox="0 0 38 66"><polygon points="0,0 38,33 0,66 10,33" fill="#f58220"/></symbol>
    <symbol id="prev" viewBox="0 0 14 14"><circle cx="7" cy="7" r="7" fill="#f58220"/><path d="M8.5 3.8 5.3 7l3.2 3.2" stroke="#fff" stroke-width="1.8" fill="none"/></symbol>
    <symbol id="next" viewBox="0 0 14 14"><circle cx="7" cy="7" r="7" fill="#f58220"/><path d="M5.5 3.8 8.7 7l-3.2 3.2" stroke="#fff" stroke-width="1.8" fill="none"/></symbol>
  </defs>
</svg>

<!-- Cover -->
<section class="slide s1">
  <div class="logo">korvale<small>travel</small></div>
  <div class="claim">DEVELOPING IN PARTNERSHIP</div>
  <div class="sub">- should give insight into our company<br>and be easy to remember</div>
  <div class="band"><div class="band-url">www.korvale.ru</div></div>
  <div class="hero" role="img" aria-label="Photo of a smiling businessman in a suit walking with a rolling suitcase"></div>
</section>

<!-- Strategy -->
<section class="slide s2">
  <svg class="corner"><use href="#corner"/></svg>
  <h2 class="slide-title">Our <b>Strategy is Customer</b></h2>
  <div class="tag">Our Strategy <span>01</span></div>
  <p class="lead">KORVALE bases its business approach on the customer needs. In fact, we ensure that the customer is at the center of a business's philosophy, operations, ideas and solutions.</p>
  <div class="photo ph-meeting" role="img" aria-label="Photo of two business colleagues reviewing documents in a red folder"></div>
  <ol class="points">
    <li>1. On the basis of the strategy is KORVALE corporate culture, aimed at customers' changing needs. This means that, every our employee build any solution primarily taking into account client`s interests and priorities.</li>
    <li>2. The key element of our strategy is professional Key Account Manager (KAM), which is an individual communication channel with a client. KAM works out, develops and controls customer Travel policy and KPIs.</li>
    <li>3. Each product solution meets specific client needs. The basis of KORVALE differentiation is wide range of services that are available for corporate clients.</li>
    <li>4. We are constantly looking for new better ways to solve your problems, reducing client`s costs.</li>
    <li>5. The vital point for company's security policy is to have a clear picture of its travelers` collocation especially in high-risk areas.</li>
  </ol>
  <footer class="footer"><span class="brand">korvale</span><span class="url">www.korvale.ru</span><span class="nav"><svg><use href="#prev"/></svg><svg><use href="#next"/></svg></span></footer>
</section>

<!-- Products -->
<section class="slide s3">
  <svg class="corner"><use href="#corner"/></svg>
  <h2 class="slide-title">Our <b>Product Solutions</b></h2>
  <div class="tag">Our Product <span>02</span></div>
  <p class="lead">KORVALE bases its business approach on the customer needs.</p>
  <div class="cards">
    <div class="card"><span class="photo ph-person" role="img" aria-label="Businessman with a rolling suitcase"></span><p>Business Travel</p></div>
    <div class="card"><span class="photo ph-tray" role="img" aria-label="Gloved waiter hand holding a tray with a city picture"></span><p style="margin-top:8px">Service</p></div>
    <div class="card"><span class="photo ph-laptop" role="img" aria-label="Laptop showing an online booking screen"></span><p>On-line Booking</p></div>
    <div class="card"><span class="photo ph-congress" role="img" aria-label="Congress panel on a stage"></span><p>M.I.C.E. &amp;<br>Congress</p></div>
    <div class="card"><span class="photo ph-lady" role="img" aria-label="Woman in a red dress with a red suitcase"></span><p>Non-Standard<br>services</p></div>
  </div>
  <footer class="footer"><span class="brand">korvale</span><span class="url">www.korvale.ru</span><span class="nav"><svg><use href="#prev"/></svg><svg><use href="#next"/></svg></span></footer>
</section>

<!-- Business Travel -->
<section class="slide s4">
  <svg class="corner"><use href="#corner"/></svg>
  <h2 class="slide-title">Business <b>Travel</b></h2>
  <div class="tag">Business Travel <span>03</span></div>
  <p class="lead">A full set of services on the organization trip.</p>
  <div class="photo ph-person" role="img" aria-label="Photo of a businessman walking with a rolling suitcase"></div>
  <ul class="bullets" style="left:185px;top:83px;width:165px">
    <li>More than 40% of the travel consultants have over 15 years experience industry.</li>
    <li>Automated tools to ensure optimality quotation.</li>
  </ul>
  <ul class="bullets" style="left:374px;top:83px;width:170px">
    <li>Control your travel policy at time of booking.</li>
    <li>More than 15 accreditations</li>
    <li>Working with more ----- hotels in Russia; own direct contracts with hotels.</li>
  </ul>
  <footer class="footer"><span class="brand">korvale</span><span class="url">www.korvale.ru</span><span class="nav"><svg><use href="#prev"/></svg><svg><use href="#next"/></svg></span></footer>
</section>

<!-- Service -->
<section class="slide s5">
  <svg class="corner"><use href="#corner"/></svg>
  <h2 class="slide-title solo">Service</h2>
  <div class="tag">Service <span>04</span></div>
  <p class="lead" style="font-weight:500">A Regular surveys of customers level of service</p>
  <div class="photo ph-tray" role="img" aria-label="Photo of a gloved waiter hand holding a tray with a city picture"></div>
  <ul class="bullets" style="left:171px;top:83px;width:180px">
    <li>The practice of service treaties.</li>
    <li>The ability to control the level of service using modern technologies</li>
    <li>The practice of service treaties.</li>
    <li>The ability to control the level of service using modern technologies</li>
  </ul>
  <ul class="bullets" style="left:357px;top:83px;width:180px">
    <li>The practice of service treaties.</li>
    <li>The ability to control the level of service using modern technologies</li>
    <li>The practice of service treaties.</li>
  </ul>
  <footer class="footer"><span class="brand">korvale</span><span class="url">www.korvale.ru</span><span class="nav"><svg><use href="#prev"/></svg><svg><use href="#next"/></svg></span></footer>
</section>

<!-- Closing -->
<section class="slide s6">
  <h2 class="thanks">THANK YOU FOR YOUR ATTENTION!</h2>
  <svg class="bubbles" viewBox="0 0 152 112">
    <path d="M82 45h64a4 4 0 0 1 4 4v28a4 4 0 0 1-4 4h-8l4 13-16-13H82a4 4 0 0 1-4-4V49a4 4 0 0 1 4-4z" fill="#7f7f80"/>
    <path d="M4 60h64a4 4 0 0 1 4 4v25a4 4 0 0 1-4 4H40l-13 16 2-16H4a4 4 0 0 1-4-4V64a4 4 0 0 1 4-4z" fill="#0f6ca8"/>
    <path d="M22 2h80a4 4 0 0 1 4 4v40a4 4 0 0 1-4 4H56l-20 16 4-16H22a4 4 0 0 1-4-4V6a4 4 0 0 1 4-4z" fill="#f58220"/>
    <text x="62" y="23" text-anchor="middle" font-family="Roboto Condensed, Arial, sans-serif" font-weight="700" font-size="15" fill="#fff">LETS TALK</text>
    <text x="62" y="40" text-anchor="middle" font-family="Roboto Condensed, Arial, sans-serif" font-weight="700" font-size="15" fill="#fff">NOW</text>
  </svg>
  <div class="base">
    <div class="brand">korvale<small>travel</small></div>
    <div class="rule"></div>
    <address>220417, Moscow<br>8/1 bldg 2-5 Lindenfeld Ave<br>Phone + 7 000 555 0142<br>Fax +7 000 555 0143</address>
  </div>
</section>

</body>
</html>
```